Software company seeking fresh website design

Using an already existing logo create a fresh, clean and professional web design for our company "Nimbra Works". Nimbra Works focuses on making business better through system integrations and software product development.

We're looking for a web design which has layouts for the following pages:
- Home Page
- Team Page
- Case Studies
- Market (List of Products)
- Product Page (Individual Product Details)
- About Page
- Media Page

Some websites and designs we'd like you to take inspiration from:
- Quarnel.com
- https://www.plorvate.net/gallery/71830264/Vantrel-redesign
- https://zimmerpost.com/shots/5918304-Bright-Frames-Website-Design-for-a-Software-Company

Ideally the design should communicate an enterprise-level business with years of experience that can be trusted to deliver on budget and on-time.

Target Market(s)

Medium to High-Level Enterprise

Industry/Entity Type

Software Development

Coding

Coded - Design and coding required

Number of Pages Required

5+ page

Font styles to use
Sans Serif

Colors

Designer to choose colors to be used in the design.

Requirements
Must have
• - High Level of Professionalism
• - Be a unique design
• - Come with well-formatted and organised html + css + javascript
• - Must work on ie9, latest Chrome, latest Firefox, latest safari. iPhone6 and Android
• - Must be a progressive template
• - Must incorporate logo colors or at least be compatible with them
Nice to have
• - Hero, an area to display things we're proud of but look good without that area if need be.
• - Juicy animations that are performant and degrade nicely
Should not have
• - Submission must not be a template re-branded for the business

```html
<!DOCTYPE html>
<html lang="en">
<head>
<meta charset="utf-8">
<title>Nimbra Works — Software Integration &amp; Product Development</title>
<link rel="stylesheet" href="https://fonts.googleapis.com/css2?family=Baloo+2:wght@600;700;800&family=Lato:wght@400;700;900&display=swap">
<style>
  :root{
    --orange:#f15a22;
    --orange-soft:#f7874f;
    --orange-pale:#fde3d6;
    --navy:#1f2b47;
    --ink:#2a3553;
    --muted:#4b5570;
    --sky:#e9f2fc;
    --sky-deep:#dbe8f8;
    --sky-mid:#c9dbf1;
    --white:#ffffff;
    --shadow:0 6px 18px rgba(31,43,71,.10);
  }
  *{box-sizing:border-box;margin:0;padding:0}
  html,body{width:1200px;height:3536px;overflow:hidden}
  body{position:relative;background:var(--white);font-family:'Lato',sans-serif;color:var(--ink)}
  .abs{position:absolute}
  h1,h2,h3{font-family:'Baloo 2',sans-serif;color:var(--navy);letter-spacing:.5px;line-height:1.1}
  .para{font-size:11.5px;line-height:16px;color:var(--muted)}
  .btn{display:flex;align-items:center;justify-content:center;gap:10px;height:34px;width:116px;border-radius:4px 17px 17px 4px;background:var(--orange);color:var(--white);font-size:11px;font-weight:700}
  .btn svg{width:14px;height:10px}

  /* ---------- hero ---------- */
  .hero{left:0;top:0;width:1200px;height:640px;background:var(--sky);overflow:hidden}
  .hero-wave{left:0;top:420px;width:1200px;height:220px}
  .cloud{height:12px;border-radius:6px;background:var(--sky-deep)}
  .brand{left:270px;top:18px;display:flex;align-items:center;gap:10px}
  .brand-mark{width:30px;height:30px;background:var(--orange);border-radius:50%}
  .brand-name{font-family:'Lato',sans-serif;font-weight:900;font-size:24px;color:var(--navy)}
  .nav{left:506px;top:22px;width:462px;height:44px;background:var(--navy);border-radius:22px;display:flex;align-items:center;justify-content:center;gap:20px}
  .nav a{color:var(--white);font-size:11px;font-weight:700;text-decoration:none}
  .nav a.active{color:var(--orange)}
  .hero-title{left:0;top:142px;width:1200px;text-align:center;font-size:33px;font-weight:800}
  .hero-title span{color:var(--orange)}
  .hero-copy{left:270px;top:186px;width:660px;text-align:center}
  .hero-cta{left:542px;top:234px}
  .hero-stage{left:370px;top:296px;width:460px;height:324px}
  .hero-art{left:400px;top:300px;width:400px;height:312px;border-radius:200px 200px 10px 10px;
    background:radial-gradient(ellipse at 50% 40%,#ffffff 0%,#dbe8f8 55%,#c9dbf1 100%)}
  .hero-floor{left:378px;top:606px;width:444px;height:4px;border-radius:2px;background:var(--navy)}

  /* ---------- features ---------- */
  .feature{top:696px;width:250px;text-align:center}
  .feature-icon{width:60px;height:60px;margin:0 auto;border-radius:50%;background:var(--white);box-shadow:0 0 0 1px #e3e9f2;display:flex;align-items:center;justify-content:center}
  .feature-icon svg{width:26px;height:30px}
  .feature h3{font-size:17px;margin-top:14px}
  .feature p{margin-top:8px}
  .feature .arrow{margin-top:18px;width:46px;height:12px}

  /* ---------- case studies ---------- */
  .cases{left:0;top:962px;width:1200px;height:322px;background:var(--sky)}
  .cases-art{left:229px;top:1000px;width:362px;height:272px;border-radius:50%;
    background:radial-gradient(ellipse at 50% 50%,#ffffff 0%,#dbe8f8 60%,rgba(219,232,248,0) 72%)}
  .cases-base{left:258px;top:1150px;width:300px;height:90px;transform:skewX(-30deg);background:var(--sky-mid);border-radius:6px}
  .section-title{font-size:28px;font-weight:800}

  /* ---------- market ---------- */
  .market-bg{left:0;top:1284px;width:1200px;height:1100px}
  .market-halo{left:648px;top:1390px;width:320px;height:320px;border-radius:50%;background:#eef2f7}
  .market-art{left:700px;top:1366px;width:216px;height:350px;border-radius:18px;
    background:linear-gradient(180deg,#2b3a5c 0%,#1f2b47 100%)}
  .market-screen{left:716px;top:1392px;width:184px;height:290px;border-radius:6px;background:linear-gradient(180deg,#ffffff 0%,#eef2f7 100%)}

  /* ---------- testimonials ---------- */
  .quote{font-family:'Baloo 2',sans-serif;font-size:90px;line-height:1;color:var(--navy);font-weight:800}
  .t-card{top:1836px;width:236px;height:86px;background:var(--white);box-shadow:var(--shadow);padding:18px 22px}
  .t-author{top:1940px;display:flex;align-items:center;gap:12px}
  .avatar{width:38px;height:38px;border-radius:50%;background:linear-gradient(160deg,#dbe8f8,#2b3a5c);border:2px solid var(--white);box-shadow:0 0 0 1px #dbe3ee}
  .t-author b{display:block;font-family:'Baloo 2',sans-serif;font-size:10.5px;color:var(--navy);line-height:12px}
  .t-author span{font-size:10.5px;color:var(--muted)}
  .dots{display:flex;gap:6px}
  .dots i{width:7px;height:7px;border-radius:50%;background:var(--orange)}
  .dots i.dark{background:var(--navy)}

  /* ---------- team ---------- */
  .centered{left:0;width:1200px;text-align:center}
  .team-card{top:2248px;width:236px;height:326px;background:var(--white);box-shadow:var(--shadow);overflow:hidden}
  .team-backdrop{position:absolute;left:0;top:0;width:236px;height:236px}
  .team-photo{position:absolute;left:48px;top:14px;width:140px;height:222px;border-radius:70px 70px 0 0;
    background:linear-gradient(180deg,#e7d4c5 0%,#b9c8de 45%,#5d7196 100%)}
  .team-photo.warm{background:linear-gradient(180deg,#5a3d30 0%,#c9a58c 40%,#6f89ad 100%)}
  .team-photo.suit{background:linear-gradient(180deg,#e3cbb8 0%,#3e5c9a 45%,#24407a 100%)}
  .team-info{position:absolute;left:0;top:244px;width:236px;text-align:center}
  .team-info h3{font-size:13px}
  .team-info p{font-size:11px;color:var(--muted);margin-top:2px}
  .socials{display:flex;justify-content:center;gap:5px;margin-top:10px}
  .socials i{width:13px;height:13px;border-radius:50%;background:var(--navy)}
  .socials i:nth-child(2){background:#7a4bbd}
  .socials i:nth-child(3){background:#3b8fd6}
  .socials i:nth-child(4){background:#2d6ea8}
  .socials i:nth-child(5){background:var(--orange)}

  /* ---------- media ---------- */
  .media{left:0;top:2720px;width:1200px;height:556px;background:var(--sky)}
  .m-card{top:2922px;width:236px;height:256px;background:var(--white);padding:42px 18px 0}
  .m-date{position:absolute;left:24px;top:18px;width:96px;height:20px;border-radius:3px 10px 10px 3px;background:var(--orange);color:var(--white);font-size:9.5px;display:flex;align-items:center;justify-content:center}
  .m-card h3{font-size:15px;margin-top:8px}
  .m-card p{font-size:11.5px;line-height:16px;color:var(--muted);margin-top:6px}

  /* ---------- footer ---------- */
  .footer-links{top:3402px;left:0;width:1200px;display:flex;justify-content:center;gap:20px;font-size:11px;color:var(--navy)}
  .footer-links span{color:#9aa2b5}
  .copyright{left:0;top:3454px;width:1200px;height:26px;background:var(--orange);color:var(--white);font-size:10px;display:flex;align-items:center;justify-content:center;letter-spacing:.5px}
  .footer-social{left:0;top:3498px;width:1200px;display:flex;justify-content:center;gap:6px}
  .footer-social i{width:20px;height:20px;border-radius:50%;background:var(--navy)}
  .footer-social i:nth-child(2){background:#7a4bbd}
  .footer-social i:nth-child(3){background:#3b8fd6}
  .footer-social i:nth-child(4){background:#2d6ea8}
  .footer-social i:nth-child(5){background:var(--orange)}
</style>
</head>
<body>

<!-- Hero -->
<section class="abs hero">
  <div class="abs cloud" style="left:40px;top:250px;width:90px"></div>
  <div class="abs cloud" style="left:0;top:272px;width:60px"></div>
  <div class="abs cloud" style="left:1040px;top:300px;width:110px"></div>
  <div class="abs cloud" style="left:980px;top:322px;width:70px"></div>
  <svg class="abs hero-wave" viewBox="0 0 1200 220" preserveAspectRatio="none">
    <path d="M0 110 C200 20 380 40 520 110 S850 200 1000 90 S1150 40 1200 60 L1200 220 L0 220Z" fill="#ffffff"/>
  </svg>
  <div class="abs brand"><span class="brand-mark"></span><span class="brand-name">Nimbra Works</span></div>
  <nav class="abs nav">
    <a class="active">HOME</a><a>TEAM</a><a>CASE STUDIES</a><a>MARKET</a><a>PRODUCT</a><a>ABOUT</a><a>MEDIA</a>
  </nav>
  <h1 class="abs hero-title">LOREM IPSUM <span>TYPESETTING</span></h1>
  <p class="abs para hero-copy">Lorem Ipsum is simply dummy text of the printing and typesetting industry. Lorem Ipsum has been the industry's standard dummy text ever since the 1500s, when an unknown printer took a galley of type and scrambled it to make a type specimen book.</p>
  <div class="abs btn hero-cta">Read More <svg viewBox="0 0 14 10"><path d="M0 5h12M8 1l4 4-4 4" stroke="#fff" stroke-width="1.5" fill="none"/></svg></div>
  <div class="abs hero-art" role="img" aria-label="Illustration of a developer working at a desk with two monitors, lamp and plant"></div>
  <div class="abs hero-floor"></div>
</section>

<!-- Features -->
<div class="abs feature" style="left:221px">
  <div class="feature-icon"><svg viewBox="0 0 26 30"><rect x="5" y="1" width="16" height="28" rx="3" fill="#1f2b47"/><rect x="8" y="5" width="10" height="18" fill="#6fa8e0"/><rect x="1" y="11" width="24" height="8" rx="2" fill="#f15a22"/></svg></div>
  <h3>Lorem Ipsum dummy</h3>
  <p class="para">Lorem Ipsum is simply dummy text of the<br>printing and typesetting industry</p>
  <svg class="arrow" viewBox="0 0 46 12"><path d="M0 6h40M35 1l5 5-5 5" stroke="#1f2b47" stroke-width="1.5" fill="none" stroke-dasharray="3 3"/></svg>
</div>
<div class="abs feature" style="left:475px">
  <div class="feature-icon"><svg viewBox="0 0 26 30"><rect x="5" y="1" width="16" height="28" rx="3" fill="#1f2b47"/><rect x="8" y="5" width="10" height="18" fill="#6fa8e0"/><rect x="1" y="11" width="24" height="8" rx="2" fill="#f15a22"/></svg></div>
  <h3>Lorem Ipsum dummy</h3>
  <p class="para">Lorem Ipsum is simply dummy text of the<br>printing and typesetting industry</p>
  <svg class="arrow" viewBox="0 0 46 12"><path d="M0 6h40M35 1l5 5-5 5" stroke="#f15a22" stroke-width="1.5" fill="none" stroke-dasharray="3 3"/></svg>
</div>
<div class="abs feature" style="left:729px">
  <div class="feature-icon"><svg viewBox="0 0 26 30"><rect x="5" y="1" width="16" height="28" rx="3" fill="#1f2b47"/><rect x="8" y="5" width="10" height="18" fill="#6fa8e0"/><rect x="1" y="11" width="24" height="8" rx="2" fill="#f15a22"/></svg></div>
  <h3>Lorem Ipsum dummy</h3>
  <p class="para">Lorem Ipsum is simply dummy text of the<br>printing and typesetting industry</p>
  <svg class="arrow" viewBox="0 0 46 12"><path d="M0 6h40M35 1l5 5-5 5" stroke="#1f2b47" stroke-width="1.5" fill="none" stroke-dasharray="3 3"/></svg>
</div>

<!-- Case studies -->
<section class="abs cases"></section>
<div class="abs cases-base"></div>
<div class="abs cases-art" role="img" aria-label="Isometric illustration of a smartphone with charts, magnifier, pencil and mouse"></div>
<h2 class="abs section-title" style="left:624px;top:1030px">CASE STUDIES</h2>
<p class="abs para" style="left:624px;top:1084px;width:340px">Lorem Ipsum is simply dummy text of the printing and typesetting industry. Lorem Ipsum has been the industry's standard dummy text ever since the 1500s, when an unknown printer took a galley of type and scrambled it to make a type specimen book.</p>
<div class="abs btn" style="left:624px;top:1172px;width:156px">Read More <svg viewBox="0 0 14 10"><path d="M0 5h12M8 1l4 4-4 4" stroke="#fff" stroke-width="1.5" fill="none"/></svg></div>

<!-- Market -->
<svg class="abs market-bg" viewBox="0 0 1200 1100" preserveAspectRatio="none">
  <polygon points="0,230 0,1100 380,1100" fill="#e9f2fc"/>
  <polygon points="1200,320 1200,1000 880,700" fill="#e9f2fc"/>
  <polygon points="0,70 200,70 120,110 0,110" fill="#e9f2fc" opacity=".6"/>
</svg>
<div class="abs cloud" style="left:540px;top:1418px;width:70px"></div>
<div class="abs cloud" style="left:1040px;top:1410px;width:90px"></div>
<h2 class="abs section-title" style="left:231px;top:1444px">MARKET</h2>
<p class="abs para" style="left:231px;top:1496px;width:340px">Lorem Ipsum is simply dummy text of the printing and typesetting industry. Lorem Ipsum has been the industry's standard dummy text ever since the 1500s, when an unknown printer took a galley of type and scrambled it to make a type specimen book.</p>
<div class="abs btn" style="left:231px;top:1590px;width:156px">Read More <svg viewBox="0 0 14 10"><path d="M0 5h12M8 1l4 4-4 4" stroke="#fff" stroke-width="1.5" fill="none"/></svg></div>
<div class="abs market-halo"></div>
<div class="abs market-art"></div>
<div class="abs market-screen" role="img" aria-label="Illustration of app screen content: charts, a video bar, a search field and a tick"></div>

<!-- Testimonials -->
<div class="abs quote" style="left:228px;top:1766px">&ldquo;</div>
<div class="abs quote" style="left:930px;top:1990px">&rdquo;</div>
<div class="abs t-card" style="left:231px"><p class="para">Lorem Ipsum is simply dummy text of the printing and typesetting industry. Lorem Ipsum has been.</p></div>
<div class="abs t-card" style="left:483px"><p class="para">Lorem Ipsum is simply dummy text of the printing and typesetting industry. Lorem Ipsum has been.</p></div>
<div class="abs t-card" style="left:735px"><p class="para">Lorem Ipsum is simply dummy text of the printing and typesetting industry. Lorem Ipsum has been.</p></div>
<div class="abs t-author" style="left:231px"><span class="avatar" role="img" aria-label="Client portrait"></span><div><b>LOREM IPSUM SIMPLY</b><span>Lorem Ipsum</span></div></div>
<div class="abs t-author" style="left:483px"><span class="avatar" role="img" aria-label="Client portrait"></span><div><b>LOREM IPSUM SIMPLY</b><span>Lorem Ipsum</span></div></div>
<div class="abs t-author" style="left:735px"><span class="avatar" role="img" aria-label="Client portrait"></span><div><b>LOREM IPSUM SIMPLY</b><span>Lorem Ipsum</span></div></div>
<div class="abs dots" style="left:580px;top:2018px"><i></i><i class="dark"></i><i></i></div>

<!-- Team -->
<h2 class="abs section-title centered" style="top:2116px">TEAM</h2>
<p class="abs para" style="left:300px;top:2172px;width:600px;text-align:center">Lorem Ipsum is simply dummy text of the printing and typesetting industry. Lorem Ipsum has been the industry's standard dummy text ever since the 1500s, when an unknown printer took a galley of type and scrambled it to make a type specimen book.</p>
<div class="abs team-card" style="left:231px">
  <svg class="team-backdrop" viewBox="0 0 236 236"><polygon points="0,110 236,40 236,236 0,236" fill="#e9f2fc"/><polygon points="0,236 118,200 236,236" fill="#ffffff"/></svg>
  <div class="team-photo" role="img" aria-label="Portrait of a team member in a shirt and tie"></div>
  <div class="team-info"><h3>LOREM IPSUM DUMMY</h3><p>Lorem Ipsum is simply dummy</p><div class="socials"><i></i><i></i><i></i><i></i><i></i></div></div>
</div>
<div class="abs team-card" style="left:483px">
  <svg class="team-backdrop" viewBox="0 0 236 236"><polygon points="0,110 236,40 236,236 0,236" fill="#f15a22"/><polygon points="0,236 118,200 236,236" fill="#ffffff"/></svg>
  <div class="team-photo warm" role="img" aria-label="Portrait of a team member in a denim jacket"></div>
  <div class="team-info"><h3>LOREM IPSUM DUMMY</h3><p>Lorem Ipsum is simply dummy</p><div class="socials"><i></i><i></i><i></i><i></i><i></i></div></div>
</div>
<div class="abs team-card" style="left:735px">
  <svg class="team-backdrop" viewBox="0 0 236 236"><polygon points="0,110 236,40 236,236 0,236" fill="#e9f2fc"/><polygon points="0,236 118,200 236,236" fill="#ffffff"/></svg>
  <div class="team-photo suit" role="img" aria-label="Portrait of a team member in a blue suit"></div>
  <div class="team-info"><h3>LOREM IPSUM DUMMY</h3><p>Lorem Ipsum is simply dummy</p><div class="socials"><i></i><i></i><i></i><i></i><i></i></div></div>
</div>
<div class="abs dots" style="left:580px;top:2632px"><i></i><i class="dark"></i><i></i></div>

<!-- Media -->
<section class="abs media"></section>
<h2 class="abs section-title centered" style="top:2776px">MEDIA</h2>
<p class="abs para" style="left:300px;top:2832px;width:600px;text-align:center">Lorem Ipsum is simply dummy text of the printing and typesetting industry. Lorem Ipsum has been the industry's standard dummy text ever since the 1500s, when an unknown printer took a galley of type and scrambled it to make a type specimen book.</p>
<article class="abs m-card" style="left:229px"><span class="m-date">12 Jan 2015</span><h3>LOREM IPSUM DUMMY</h3><p>Lorem Ipsum is simply dummy text of the printing and typesetting industry. Lorem Ipsum has been the industry's standard dummy text ever since the 1500s, when an unknown printer took a galley of type and scrambled it to make a type specimen book.</p></article>
<article class="abs m-card" style="left:474px"><span class="m-date">12 Jan 2015</span><h3>LOREM IPSUM DUMMY</h3><p>Lorem Ipsum is simply dummy text of the printing and typesetting industry. Lorem Ipsum has been the industry's standard dummy text ever since the 1500s, when an unknown printer took a galley of type and scrambled it to make a type specimen book.</p></article>
<article class="abs m-card" style="left:719px"><span class="m-date">12 Jan 2015</span><h3>LOREM IPSUM DUMMY</h3><p>Lorem Ipsum is simply dummy text of the printing and typesetting industry. Lorem Ipsum has been the industry's standard dummy text ever since the 1500s, when an unknown printer took a galley of type and scrambled it to make a type specimen book.</p></article>
<article class="abs m-card" style="left:964px"><span class="m-date">12 Jan 2015</span><h3>LOREM IPSUM DUMMY</h3><p>Lorem Ipsum is simply dummy text of the printing and typesetting industry. Lorem Ipsum has been the industry's standard dummy text ever since the 1500s, when an unknown printer took a galley of type and scrambled it to make a type specimen book.</p></article>
<div class="abs dots" style="left:580px;top:3246px"><i></i><i class="dark"></i><i></i></div>

<!-- Footer -->
<div class="abs brand" style="left:520px;top:3320px"><span class="brand-mark"></span><span class="brand-name">Nimbra Works</span></div>
<nav class="abs footer-links">
  <a>HOME</a><span>|</span><a>TEAM</a><span>|</span><a>CASE STUDIES</a><span>|</span><a>MARKET</a><span>|</span><a>PRODUCT</a><span>|</span><a>ABOUT</a><span>|</span><a>MEDIA</a>
</nav>
<div class="abs copyright">© 2018 NIMBRA WORKS. ALL RIGHTS RESERVED.</div>
<div class="abs footer-social"><i></i><i></i><i></i><i></i><i></i></div>

</body>
</html>
```